Business Card Design

Company name is: Ridgeline Lifeguard Training, LLC. We teach CPR/AED, First Aid, Bloodborne Pathogens and other health and safety classes. Looking for an eye-catching, progressive, cutting edge design.

Industry/Entity Type

Health

Contact Information for Business Card

Tom Wexford (555.218.4073)
June Pellicott (555.862.1940)
email is info@ridgelinetraininghq.com
website is www.RidgelineTrainingHQ.com

```html
<!DOCTYPE html>
<html lang="en">
<head>
<meta charset="utf-8">
<title>Ridgeline Lifeguard Training, LLC — Business Card</title>
<link rel="stylesheet" href="https://fonts.googleapis.com/css2?family=Libre+Baskerville:wght@400;700&display=swap">
<style>
  :root {
    --page-bg: #d9d9d9;
    --card-white: #f7f7f5;
    --brand-blue: #0f6db3;
    --brand-red: #c8161d;
    --text-white: #ffffff;
  }
  html, body {
    margin: 0;
    padding: 0;
    width: 1200px;
    height: 1200px;
    overflow: hidden;
    background: var(--page-bg);
  }
  .canvas {
    position: relative;
    width: 1200px;
    height: 1200px;
    display: flex;
    align-items: center;
    justify-content: center;
  }
  .business-card {
    position: relative;
    width: 1000px;
    height: 572px;
    background: var(--card-white);
    overflow: hidden;
    box-shadow: 0 6px 18px rgba(0,0,0,0.18);
    font-family: "Libre Baskerville", "Bookman Old Style", Georgia, serif;
  }
  .company-name {
    position: absolute;
    top: 118px;
    left: 0;
    right: 0;
    margin: 0;
    display: flex;
    align-items: center;
    justify-content: center;
    gap: 16px;
    color: var(--brand-red);
    font-weight: 400;
    font-size: 40px;
    letter-spacing: 0.3px;
  }
  .company-mark {
    width: 22px;
    height: 22px;
    border-radius: 50%;
    background: var(--brand-red);
    flex: none;
  }
  .skyline-band {
    position: absolute;
    left: 0;
    right: 0;
    top: 215px;
    bottom: 0;
    background: var(--brand-blue);
  }
  .contact {
    position: absolute;
    color: var(--text-white);
  }
  .contact-name {
    margin: 0 0 10px;
    font-weight: 700;
    font-size: 27px;
  }
  .contact-line {
    display: flex;
    align-items: center;
    gap: 14px;
    font-size: 25px;
    margin: 0;
  }
  .icon {
    width: 24px;
    height: 24px;
    flex: none;
  }
  .contact-left { left: 80px; top: 262px; }
  .contact-right { left: 580px; top: 392px; }
  .contact-email { left: 46px; top: 435px; }
  .contact-web { left: 314px; top: 486px; }
</style>
</head>
<body>
<main class="canvas">
  <article class="business-card">
    <h1 class="company-name"><span class="company-mark"></span>Ridgeline Lifeguard Training, LLC</h1>

    <div class="skyline-band" role="img" aria-label="City skyline silhouette in brand blue"></div>

    <section class="contact contact-left">
      <p class="contact-name">Tom Wexford</p>
      <p class="contact-line">
        <svg class="icon" viewBox="0 0 24 24" aria-hidden="true">
          <circle cx="12" cy="12" r="12" fill="var(--brand-red)"/>
          <path d="M8 6.5c.6-.4 1.3-.3 1.6.3l1 1.8c.3.5.2 1.1-.3 1.4l-.8.6c.6 1.4 1.6 2.5 3 3.1l.6-.8c.3-.5.9-.6 1.4-.3l1.8 1c.6.3.7 1 .3 1.6l-.7.9c-.5.6-1.3.8-2 .5-3.1-1.3-5.5-3.7-6.8-6.8-.3-.7-.1-1.5.5-2z" fill="#fff"/>
        </svg>
        555.218.4073
      </p>
    </section>

    <section class="contact contact-right">
      <p class="contact-name">June Pellicott</p>
      <p class="contact-line">
        <svg class="icon" viewBox="0 0 24 24" aria-hidden="true">
          <circle cx="12" cy="12" r="12" fill="var(--brand-red)"/>
          <path d="M8 6.5c.6-.4 1.3-.3 1.6.3l1 1.8c.3.5.2 1.1-.3 1.4l-.8.6c.6 1.4 1.6 2.5 3 3.1l.6-.8c.3-.5.9-.6 1.4-.3l1.8 1c.6.3.7 1 .3 1.6l-.7.9c-.5.6-1.3.8-2 .5-3.1-1.3-5.5-3.7-6.8-6.8-.3-.7-.1-1.5.5-2z" fill="#fff"/>
        </svg>
        555.862.1940
      </p>
    </section>

    <p class="contact contact-line contact-email">
      <svg class="icon" viewBox="0 0 24 24" aria-hidden="true">
        <circle cx="12" cy="12" r="12" fill="var(--brand-red)"/>
        <rect x="6" y="8" width="12" height="8.5" rx="1" fill="#fff"/>
        <path d="M6.5 8.6l5.5 4.2 5.5-4.2" fill="none" stroke="var(--brand-red)" stroke-width="1.2"/>
      </svg>
      info@ridgelinetraininghq.com
    </p>

    <p class="contact contact-line contact-web">
      <svg class="icon" viewBox="0 0 24 24" aria-hidden="true">
        <circle cx="12" cy="12" r="12" fill="var(--brand-red)"/>
        <g fill="none" stroke="#fff" stroke-width="1.3">
          <circle cx="12" cy="12" r="6.5"/>
          <ellipse cx="12" cy="12" rx="3" ry="6.5"/>
          <path d="M5.5 12h13M6.5 8.8h11M6.5 15.2h11"/>
        </g>
      </svg>
      www.RidgelineTrainingHQ.com
    </p>
  </article>
</main>
</body>
</html>
```